Fundraising Study Day East of England. Lift the January blues!

A flyer to advertise a fundraising event of lectures for dental hygienists and therapists in support of the exemption campaign. Currently dental hygienists and therapists require a prescription to deliver certain treatment or recommend certain toothpastes. If we are successful in the campaign we will be able to treat patients without these restrictions.

Industry/Entity Type

Dental

```html
<!DOCTYPE html>
<html lang="en">
<head>
<meta charset="utf-8">
<title>Fundraising Study Day East of England</title>
<link rel="stylesheet" href="https://fonts.googleapis.com/css2?family=Source+Sans+3:ital,wght@0,300;0,400;0,600;0,700;1,600;1,700&family=Kaushan+Script&family=Montserrat:wght@600&display=swap">
<style>
:root{
  --royal:#3d4a9f;
  --royal-deep:#33408f;
  --paper:#f4f3ef;
  --orange:#f15a24;
  --sky:#2a9fd8;
  --ink:#1a1a1a;
  --body:#333;
  --lime:#8cc63f;
  --grey:#555;
}
*{margin:0;padding:0;box-sizing:border-box}
html,body{width:957px;height:1200px;overflow:hidden;background:#fff}
.flyer{width:957px;height:1200px;display:flex;font-family:"Source Sans 3",sans-serif}
.left{width:488px;display:flex;flex-direction:column}
.headline{height:362px;background:var(--royal);color:#fff;display:flex;align-items:center;justify-content:center;text-align:center;padding:10px 20px 10px 24px}
.headline h1{font-weight:700;font-size:49px;line-height:60px;letter-spacing:-.3px}
.hero{position:relative;height:538px;background:linear-gradient(100deg,#f4f6f8 0%,#e6ecf1 45%,#dfe6ec 70%,#cdd8e1 100%)}
.hero-photo{position:absolute;inset:0}
.hero-intro{position:absolute;left:44px;top:20px;width:150px;font-weight:300;font-size:19px;line-height:28.5px;color:var(--grey)}
.hero-web{position:absolute;right:30px;bottom:8px;font-weight:700;font-size:27px;color:#3b3b3b;letter-spacing:.3px}
.summary{flex:1;background:var(--royal-deep);color:#fff;padding:28px 30px 0 51px}
.summary p{font-size:17px;line-height:24px;text-align:justify}
.summary .link{margin-top:27px;font-weight:600;font-size:13.6px;line-height:18.5px;text-align:left;word-break:break-all}
.right{flex:1;background:var(--paper);position:relative;padding-top:38px}
.event-mark{font-family:"Kaushan Script",cursive;color:var(--orange);font-size:82px;text-align:center;line-height:90px;padding-left:10px}
.label{color:var(--sky);font-size:42px;font-weight:600;text-align:center;line-height:48px}
.detail{text-align:center;font-weight:700;font-size:23px;line-height:30px;color:var(--ink)}
.loc{margin-top:4px}
.rule{width:340px;height:1px;background:#777;margin:20px auto 20px 63px}
.agenda-band{display:block;margin:22px 0 0 12px}
.agenda{padding:22px 42px 0 42px}
.slot{color:var(--orange);font-weight:700;font-size:21px;line-height:24px;margin-top:9px}
.slot span{color:var(--body);font-weight:400}
.talk{font-size:14.4px;line-height:18.5px;color:var(--body);text-align:justify;margin-top:7px}
.talk b{font-style:italic;font-weight:700;font-size:17px;color:var(--ink)}
</style>
</head>
<body>
<main class="flyer">
  <section class="left">
    <header class="headline"><h1>Fundraising Study Day East of England. Lift the January blues!</h1></header>
    <div class="hero">
      <div class="hero-photo" role="img" aria-label="Photo of a smiling clinician in a white coat with a stethoscope, arms crossed, in a bright clinic"></div>
      <p class="hero-intro">Event of lectures for DENTAL HYGIENISTS and THERAPISTS in support of the exemption campaign.</p>
      <p class="hero-web">www.ticketsquare.co.uk</p>
    </div>
    <div class="summary">
      <p>A fundraising event to support our exemptions project. The day will consist of a series of presentations ranging from the new ECPD to new technologies. The aim, being to enhance our learning and raise funds to support the exemptions campaign. The speaker line includes some of the UK and Irelands most respected dental professionals in our field.</p>
      <p class="link">https://www.ticketsquare.co.uk/e/fundraising-study-day-east-of-england-lift-the-january-blues-tickets-48215730194</p>
    </div>
  </section>
  <section class="right">
    <div class="event-mark">Event</div>
    <h2 class="label">LOCATION</h2>
    <p class="detail loc">Larkfield Hotel, Meteor Road,<br>Welbury, WB4 7QT</p>
    <div class="rule"></div>
    <h2 class="label">Date And Time</h2>
    <p class="detail">Fri 19 January 2018<br>09:00-16:30 GMT</p>
    <svg class="agenda-band" width="457" height="55" viewBox="0 0 457 55">
      <polygon points="0,48 14,55 14,48" fill="#6a1b6e"/>
      <polygon points="178,0 457,0 457,48 150,48" fill="var(--lime)"/>
      <polygon points="170,0 182,0 154,48 142,48" fill="#fff"/>
      <polygon points="0,0 170,0 142,48 0,48" fill="var(--royal)"/>
      <text x="14" y="33" fill="#fff" font-family="Montserrat, sans-serif" font-weight="600" font-size="27">Agenda</text>
    </svg>
    <div class="agenda">
      <p class="slot">9.30 - 10.15</p>
      <p class="talk"><b>Helena Marsh:</b> Immediate past president of the NADHT will be updating us on all things ECPD</p>
      <p class="slot">10.15 - 11.00</p>
      <p class="talk"><b>Megan Thorley:</b> Will provide an update on teeth whitening and explain how social media has impacted her business</p>
      <p class="talk"><b>Annette Graves:</b> Our internationally acclaimed speaker will update our knowledge of periodontal disease and nutrition and new technologies.</p>
      <p class="slot">11.00 - 11.30 <span>Break</span></p>
      <p class="slot">11.30 - 13.00</p>
      <p class="talk"><b>Sinead Callaghan &amp; Melanie Pruett:</b> Will be providing a combined presentation on 'Scaling your business' and start to finish ultrasonic techniques. The aim being to build our business with effective communications, systems and protocols. This sessions promises audience participation!</p>
      <p class="slot">12 - 1400 <span>lunch</span></p>
      <p class="slot">14 - 15.00</p>
      <p class="talk"><b>Priya Patel:</b> Save your back. All things posture.</p>
      <p class="slot">15.00 - 15.30 <span>Break</span></p>
      <p class="slot">15.30 16.30</p>
      <p class="talk"><b>Annette Graves:</b> Our internationally acclaimed speaker will update our knowledge of periodontal disease and nutrition and new technologies.</p>
    </div>
  </section>
</main>
</body>
</html>
```